Weight gainer supplement design

Looking for a design for a weight gainer /meal replacement supplement. The black plastic tub we will use has 2 spaces for sticker one around the rim approx 2.8cm tall x 30cm wideAnother around the main tub. The main sticker size will be 18cm tall by 70cm this will include the front of the product then wrap around to show the nutritional table.The brand is KTV (Kestrel training vitals) and the product will be called ALPHA MASSThe target ordience is men aged 16-35 its should have a profesional feel to it. The product comes in a black tub, the colores we would like to use are black and blue or red or gold or silver but we are open to suggestions and would like artistic imput. Are logo for KTV is attached but can be changed if the designer prefers.Attached is 1. KTV logo2. Image of similar product that comes in the same tub3 - 5 - images of similar products that we like the design of.The product is 12lbs and will be vanilla flavor. Please ask for more suggestions if needed, I have kept this description short to try and get artistic input.Thanks in advance :)
Updates

Target Market(s)

18-35 males who go to the gym

Industry/Entity Type

Fitness

Colors

Designer to choose colors to be used in the design.

Requirements
Must have
• name bravo bulk, logo KTV
Should not have
• images of people

```html
<!DOCTYPE html>
<html lang="en">
<head>
<meta charset="UTF-8">
<title>Bravo Bulk – Label</title>
<link href="https://fonts.googleapis.com/css2?family=Open+Sans:wght@700;800&display=swap" rel="stylesheet">
<style>
  :root {
    --label-blue: #3c76ad;
    --tub-black: #060606;
    --ink-black: #0a0a0a;
    --white: #ffffff;
    --mark-grey: #3a3a3a;
    --weight-grey: #505050;
    --figure-light: #b9c3cc;
    --figure-dark: #5e5e5e;
  }
  html, body {
    margin: 0;
    padding: 0;
    overflow: hidden;
    background: var(--white);
  }
  .label {
    position: relative;
    width: 1200px;
    height: 309px;
    overflow: hidden;
    background: var(--label-blue);
    font-family: "Open Sans", Arial, sans-serif;
  }
  .seam-strip {
    position: absolute;
    left: 0; top: 0;
    width: 50px; height: 309px;
    background: var(--tub-black);
  }
  .rim-rule {
    position: absolute;
    left: 50px; top: 35px;
    width: 1150px; height: 2.5px;
    background: var(--ink-black);
  }
  .nutrition {
    position: absolute;
    left: 59px; top: 17px;
    color: var(--ink-black);
  }
  .nutrition-title {
    margin: 0;
    font-size: 18px;
    font-weight: 800;
    line-height: 22px;
  }
  .nutrition-list {
    list-style: none;
    margin: 17px 0 0;
    padding: 0;
    font-size: 10.4px;
    font-weight: 800;
    line-height: 13.2px;
  }
  .nutrition-list .sub { padding-left: 3px; }
  .front-panel {
    position: absolute;
    left: 282px; top: 88px;
    width: 930px; height: 230px;
    background: var(--tub-black);
    border-radius: 8px;
  }
  .hero-figure {
    position: absolute;
    left: 636px; top: 4px;
    width: 212px; height: 305px;
  }
  .product-name-top {
    position: absolute;
    left: 310px; top: 30px;
    margin: 0;
    color: var(--white);
    font-size: 68px;
    font-weight: 800;
    line-height: 80px;
    letter-spacing: 1px;
  }
  .tagline {
    position: absolute;
    left: 310px; top: 120px;
    margin: 0;
    color: var(--white);
    font-size: 19.5px;
    font-weight: 800;
    line-height: 26px;
  }
  .product-name-bottom {
    position: absolute;
    left: 664px; top: 168px;
    margin: 0;
    color: var(--white);
    font-weight: 800;
    line-height: 140px;
    white-space: nowrap;
  }
  .product-name-bottom .initial { font-size: 146px; }
  .product-name-bottom .rest { font-size: 78px; letter-spacing: 1px; }
  .brand-mark {
    position: absolute;
    left: 378px; top: 208px;
    color: var(--mark-grey);
    font-size: 52px;
    font-weight: 800;
    line-height: 60px;
    letter-spacing: 2px;
  }
  .net-weight {
    position: absolute;
    left: 1023px; top: 248px;
    color: var(--weight-grey);
    font-size: 17px;
    font-weight: 800;
    line-height: 22px;
  }
</style>
</head>
<body>
<div class="label">
  <div class="seam-strip"></div>
  <div class="rim-rule"></div>

  <section class="nutrition">
    <h2 class="nutrition-title">Nutrition Facts</h2>
    <ul class="nutrition-list">
      <li>Serving Size 1 cup (228g)</li>
      <li>Servings Per Container 2</li>
      <li>Amount Per Serving</li>
      <li>Calories 260 Calories from Fat 120</li>
      <li>% Daily Value*</li>
      <li>Total Fat 13g 20%</li>
      <li class="sub">Saturated Fat 5g 25%</li>
      <li class="sub">Trans Fat 2g</li>
      <li>Cholesterol 30mg 10%</li>
      <li>Sodium 660mg 28%</li>
      <li>Total Carbohydrate 31g 10%</li>
      <li class="sub">Dietary Fiber 0g 0%</li>
      <li class="sub">Sugars 5g</li>
      <li>Protein 5g</li>
      <li>Vitamin A 4% • Vitamin C 2%</li>
      <li>Calcium 15% • Iron 4%</li>
    </ul>
  </section>

  <div class="front-panel"></div>

  <svg class="hero-figure" viewBox="0 0 212 305" role="img" aria-label="Muscular athlete illustration">
    <defs>
      <linearGradient id="figureTone" x1="0" y1="0" x2="0" y2="1">
        <stop offset="0" stop-color="var(--figure-light)" stop-opacity="0.75"/>
        <stop offset="0.3" stop-color="var(--figure-dark)" stop-opacity="0.8"/>
        <stop offset="1" stop-color="var(--figure-dark)" stop-opacity="0.6"/>
      </linearGradient>
    </defs>
    <rect x="0" y="0" width="212" height="305" rx="40" fill="url(#figureTone)"/>
  </svg>

  <h1 class="product-name-top">BRAVO</h1>
  <p class="tagline">Meal replacement supplement</p>
  <p class="product-name-bottom"><span class="initial">B</span><span class="rest">ULK</span></p>

  <div class="brand-mark">KTV</div>
  <div class="net-weight">12lbs</div>
</div>
</body>
</html>
```